CoinVale Landing Page | A free, personalized stock market email

We are looking for someone to revamp our landing page at https://coinvale.example . You should get to know the product and what it offers, and present new designs for our landing page. Feel free to use assets that currently exist on the page, as well as any new assets that you can put together. This landing page should make it obvious what the product does and aim to dramatically increase our conversion rate. We are looking for creativity, uniqueness, and clarity of purpose.

Target Market(s)

People who are invested in, or interested in being invested in, the stock market

Industry/Entity Type

Finance

Number of Pages Required

1 page

Font styles to use
Sans Serif

Requirements
Must have
• Creativity, sleek/minimal design, existing color palette and logos
Nice to have
• Effective copy
Should not have
• Clutter

```html
<!DOCTYPE html>
<html lang="en">
<head>
<meta charset="utf-8">
<title>CoinVale – Do less. Know more.</title>
<link href="https://fonts.googleapis.com/css2?family=Open+Sans:wght@400;600;700&family=Lato:wght@400;700&display=swap" rel="stylesheet">
<style>
  :root {
    --cyan: #00dce4;
    --blue: #0a6fb8;
    --deep: #0565ad;
    --ink: #333333;
    --soft: #555555;
    --grey-bg: #eeeeee;
    --white: #ffffff;
    --black: #000000;
  }
  * { box-sizing: border-box; margin: 0; padding: 0; }
  html, body { width: 1200px; height: 3780px; overflow: hidden; }
  body { position: relative; background: var(--white); font-family: "Open Sans", sans-serif; color: var(--ink); }
  .abs { position: absolute; }
  a { color: inherit; }
  .btn {
    position: absolute; display: flex; align-items: center; justify-content: center;
    font-family: "Open Sans", sans-serif; font-weight: 600; text-decoration: none;
    box-shadow: 0 3px 6px rgba(0,0,0,.18);
  }
  .btn-grad { background: linear-gradient(90deg, var(--cyan), var(--blue)); color: var(--white); }
  .btn-white { background: var(--white); color: var(--blue); }
  .wordmark { font-family: "Open Sans", sans-serif; font-weight: 600; color: var(--blue); display: flex; align-items: center; gap: 10px; }
  .wordmark .dot { border-radius: 50%; background: var(--blue); }
  .grad-band { background: linear-gradient(90deg, var(--cyan), var(--deep)); }
  .placeholder { border-radius: 12px; }
  .feature { position: absolute; top: 792px; width: 290px; text-align: center; }
  .feature .icon { width: 115px; height: 115px; border-radius: 50%; margin: 0 auto; background: linear-gradient(135deg, var(--cyan), var(--deep)); box-shadow: 0 4px 8px rgba(0,0,0,.2); display: flex; align-items: center; justify-content: center; }
  .feature h3 { font-weight: 600; font-size: 22px; margin-top: 22px; color: var(--ink); }
  .feature p { font-family: "Lato", sans-serif; font-size: 14.5px; line-height: 31px; margin-top: 8px; padding: 0 6px; color: var(--soft); }
  .divider { position: absolute; top: 792px; width: 1px; height: 267px; background: #999; }
  .footer-links a { position: absolute; top: 3506px; color: var(--white); font-size: 17px; text-decoration: none; transform: translateX(-50%); }
</style>
</head>
<body>

<!-- Header -->
<header class="abs" style="left:0;top:0;width:1200px;height:85px;background:var(--white);">
  <div class="wordmark abs" style="left:98px;top:20px;font-size:34px;">
    <span class="dot" style="width:30px;height:30px;"></span>CoinVale
  </div>
  <a class="btn btn-grad" href="https://coinvale.example" style="left:989px;top:18px;width:111px;height:49px;font-size:18px;">Sign In</a>
</header>

<!-- Hero -->
<section class="hero abs" style="left:0;top:85px;width:1200px;height:680px;background:var(--grey-bg);overflow:hidden;"></section>
<div class="placeholder abs" role="img" aria-label="Phone showing a sample stock summary email with price changes, analyst ratings, indicators and news" style="left:592px;top:112px;width:376px;height:482px;background:linear-gradient(160deg,#bfe3f5,#3f9fd8);"></div>
<svg class="abs" style="left:0;top:0;" width="1200" height="770" viewBox="0 0 1200 770" aria-hidden="true">
  <defs>
    <linearGradient id="heroWave" x1="0" x2="1">
      <stop offset="0" stop-color="#00dce4"/><stop offset="1" stop-color="#0565ad"/>
    </linearGradient>
  </defs>
  <path d="M0 604 C180 700 360 724 560 690 C780 652 960 570 1200 550 L1200 770 L0 770 Z" fill="#ffffff"/>
  <path d="M0 604 C180 700 360 724 560 690 C780 652 960 570 1200 550" fill="none" stroke="url(#heroWave)" stroke-width="9"/>
</svg>

<h1 class="abs" style="left:94px;top:232px;font-size:72px;font-weight:700;line-height:72px;letter-spacing:-1px;color:#3a3a3a;">
  Do <span style="color:var(--blue);">less.</span><br><span style="color:var(--blue);">Know</span> more.
</h1>
<a class="btn btn-grad" href="https://coinvale.example" style="left:98px;top:396px;width:181px;height:49px;font-size:17px;">Sign Up For Free</a>
<a class="abs" href="https://coinvale.example" style="left:101px;top:466px;font-size:17px;">See a full email sample</a>

<!-- Features -->
<div class="feature" style="left:94px;">
  <div class="icon"><svg width="56" height="56" viewBox="0 0 56 56" fill="none" stroke="#fff" stroke-width="2.5"><rect x="6" y="10" width="38" height="36" rx="3"/><line x1="6" y1="19" x2="44" y2="19"/><circle cx="40" cy="40" r="11" fill="#0a6fb8"/><path d="M40 34v6l4 3"/></svg></div>
  <h3>Your Schedule</h3>
  <p>Customize when you get your email. Up to every half an hour during NXSE trading hours.</p>
</div>
<div class="divider" style="left:422px;"></div>
<div class="feature" style="left:456px;">
  <div class="icon"><svg width="56" height="56" viewBox="0 0 56 56" fill="none" stroke="#fff" stroke-width="2.5"><path d="M8 40h10l10 4 18-10"/><path d="M8 34h12l8 4"/><rect x="30" y="10" width="16" height="16"/><circle cx="18" cy="18" r="8"/></svg></div>
  <h3>Your Assets</h3>
  <p>Choose from thousands of assets to include in your email. QRVX, LMNT, BRKO and more!</p>
</div>
<div class="divider" style="left:782px;"></div>
<div class="feature" style="left:820px;">
  <div class="icon"><svg width="56" height="56" viewBox="0 0 56 56" fill="none" stroke="#fff" stroke-width="2.5"><rect x="6" y="8" width="44" height="34" rx="2"/><path d="M12 36V28M20 36V22M28 36V26"/><path d="M14 18l10-6 8 6 10-8"/><circle cx="40" cy="36" r="8"/></svg></div>
  <h3>All the Data</h3>
  <p>We provide as much data on assets as we can, including price, price change, analyst ratings, technical indicators, and news.</p>
</div>

<!-- Band: stop scanning -->
<section class="grad-band abs" style="left:0;top:1140px;width:1200px;height:499px;">
  <div class="placeholder abs" role="img" aria-label="Line drawing of a relaxed character lounging in a beach chair by the sea with a drink" style="left:98px;top:64px;width:503px;height:366px;background:linear-gradient(180deg,#ffffff,#eef6fa);"></div>
  <h2 class="abs" style="left:638px;top:108px;font-size:38px;font-weight:600;line-height:47px;color:var(--white);">Stop scanning charts<br>and chasing data</h2>
  <p class="abs" style="left:640px;top:214px;width:400px;font-family:'Lato',sans-serif;font-size:15px;line-height:31px;color:var(--white);">Don't bend over backwards to get the investment insights you need. You have better ways to spend your time and energy.</p>
  <a class="btn btn-white" href="https://coinvale.example" style="left:640px;top:328px;width:110px;height:52px;font-size:17px;">Sign In</a>
</section>

<!-- Stop paying -->
<h2 class="abs" style="left:0;top:1690px;width:1200px;text-align:center;font-size:39px;font-weight:600;">Stop paying for <span style="color:var(--blue);">information</span></h2>
<p class="abs" style="left:0;top:1750px;width:1200px;text-align:center;font-family:'Lato',sans-serif;font-size:20px;">Don't spend a dime on financial information, use that money for investments</p>
<a class="btn btn-grad" href="https://coinvale.example" style="left:483px;top:1795px;width:234px;height:50px;font-size:17px;">CoinVale is free. Period</a>
<div class="placeholder abs" role="img" aria-label="Line drawing of a character chasing floating stock tickers with a butterfly net across a grassy field" style="left:257px;top:1892px;width:682px;height:396px;background:linear-gradient(180deg,#ffffff,#f1f4f6);"></div>

<!-- Band: come to you -->
<section class="grad-band abs" style="left:0;top:2347px;width:1200px;height:448px;">
  <h2 class="abs" style="left:98px;top:92px;font-size:38px;font-weight:600;line-height:44px;color:var(--white);">Let the information come<br>right to you</h2>
  <p class="abs" style="left:98px;top:198px;width:440px;font-family:'Lato',sans-serif;font-size:20px;line-height:41px;color:var(--white);">We'll send you curated market insights exactly when you want them.</p>
  <a class="btn btn-white" href="https://coinvale.example" style="left:98px;top:293px;width:141px;height:50px;font-size:17px;">Contact Us</a>
  <div class="placeholder abs" role="img" aria-label="Line drawing of a character watching a winged envelope fly toward them" style="left:603px;top:60px;width:397px;height:327px;border-radius:6px;background:linear-gradient(180deg,#f0f0f0,#e6e6e6);"></div>
</section>

<!-- Closing call to action -->
<div class="placeholder abs" role="img" aria-label="Line drawing of a standing character in a suit gesturing upward" style="left:198px;top:2846px;width:176px;height:330px;background:linear-gradient(180deg,#ffffff,#f2f2f2);"></div>
<div class="wordmark abs" style="left:568px;top:2890px;font-size:44px;">
  <span class="dot" style="width:40px;height:40px;"></span>CoinVale
</div>
<h2 class="abs" style="left:567px;top:2968px;font-size:37px;font-weight:600;color:#111;">Do Less, Know More Today</h2>
<a class="btn btn-grad" href="https://coinvale.example" style="left:569px;top:3038px;width:181px;height:50px;font-size:17px;">Sign Up For Free</a>
<a class="abs" href="https://coinvale.example" style="left:569px;top:3113px;font-size:19px;">See a full email sample</a>

<!-- Footer -->
<footer class="abs" style="left:0;top:3215px;width:1200px;height:565px;">
  <svg class="abs" style="left:0;top:0;" width="1200" height="565" viewBox="0 0 1200 565" aria-hidden="true">
    <defs>
      <linearGradient id="footWave" x1="0" x2="1">
        <stop offset="0" stop-color="#00dce4"/><stop offset="1" stop-color="#0565ad"/>
      </linearGradient>
    </defs>
    <path d="M0 170 C350 150 650 0 880 12 C1000 18 1120 80 1200 118 L1200 565 L0 565 Z" fill="#000000"/>
    <path d="M0 170 C350 150 650 0 880 12 C1000 18 1120 80 1200 118" fill="none" stroke="url(#footWave)" stroke-width="9"/>
  </svg>
</footer>
<div class="wordmark abs" style="left:0;top:3368px;width:1200px;justify-content:center;font-size:68px;color:var(--cyan);">
  <span class="dot" style="width:56px;height:56px;background:var(--cyan);"></span>CoinVale
</div>
<nav class="footer-links">
  <a href="https://coinvale.example" style="left:389px;">About</a>
  <a href="https://coinvale.example" style="left:489px;">Blog</a>
  <a href="https://coinvale.example" style="left:616px;">Terms of Use</a>
  <a href="https://coinvale.example" style="left:780px;">Privacy Policy</a>
</nav>
<p class="abs" style="left:0;top:3550px;width:1200px;text-align:center;font-size:31px;line-height:41px;color:var(--white);">CoinVale is your free, personalized,<br>data-driven finance email</p>
<div class="abs" style="left:98px;top:3685px;width:1002px;height:1px;background:#555;"></div>
<p class="abs" style="left:99px;top:3715px;font-family:'Lato',sans-serif;font-size:17px;color:var(--white);">Copyright © 2023 CoinVale. All Rights Reserved</p>
<span class="abs" style="left:1024px;top:3710px;width:32px;height:32px;border-radius:50%;background:linear-gradient(135deg,var(--cyan),var(--deep));"></span>
<span class="abs" style="left:1067px;top:3710px;width:32px;height:32px;border-radius:50%;background:linear-gradient(135deg,var(--cyan),var(--deep));"></span>

</body>
</html>
```